Wordpress website design for children’s entertainment agency

What is the aim of the website?

The aim for the website is to attract potential bookers and to get them to respond to the Call to action: contact the entertainer - phone call/request a call back/completing a form.
All the information needs to be easy to access and navigate to, especially on mobile view.
The call to action needs to be clear and easy to navigate.

What I need:

Critical - This website needs to look good on all devices.
Easy navigation on a mobile device is essential so the elements need to be bold and easy to click on with a thumb (when in mobile view)

The ‘grid area’ needs to be graphics based with simple descriptions, i.e. ‘magic shows’, Circus Clowns, Face painting, Costume Characters, Party Host, Carnival Parties, Balloon Sculpting, DJ and MC, Princess Parties, Holiday Parties, Fun Add Ons and Contact.

See: http://www.merrylopkin.com/
and http://tottlejoyworks.com/

I would like to see a sample page layout as well to see how your design would be carried through the site layout in the inside pages.

Target Market(s)

The site visitors are mainly mums, aged between 25 - 41. Other visitors will included event organisers looking for entertainment services for baptism, communions and sweet 16’s

Industry/Entity Type

Entertainment Industry

Number of Pages Required

1 page

Font styles to use
Sans Serif

Colors
6c459b
fbed22
0493ce

Requirements
Must have
• Critical - This website needs to look good on all devices.
• Easy navigation on a mobile device is essential so the elements need to be bold and easy to click on with a thumb (when in mobile view)
• The ‘grid area’ needs to be graphics based with simple descriptions, i.e. ‘magic shows’, Circus Clowns, Face painting, Costume Characters, Party Host, Carnival Parties, Balloon Sculpting, DJ and MC, Princess Parties, Holiday Parties, Fun Add Ons and Contact.
• See: http://www.merrylopkin.com/
• and http://tottlejoyworks.com/
Nice to have
• clean looking and fun with an element of ‘Brambo’ and stars (this is the exciting site http://quindlesplaybarn.com/index.html)

```html
<!DOCTYPE html>
<html lang="en">
<head>
<meta charset="utf-8">
<title>Quindles Play Barn – Family Entertainment</title>
<link rel="stylesheet" href="https://fonts.googleapis.com/css2?family=Montserrat:wght@400;500;600;700;800&display=swap">
<style>
:root{
  --purple:#6c459b;
  --purple-dark:#4f2f7a;
  --yellow:#fbed22;
  --blue:#0493ce;
  --blue-tile:#1596d2;
  --tile-light:#e6f3fa;
  --tile-mid:#8fcbea;
  --tile-dark:#12263a;
  --header-bg:#f4f4f4;
  --gray-bg:#e0e0e0;
  --charcoal:#363636;
  --ink:#111111;
  --heading-gray:#454545;
  --white:#ffffff;
}
*{box-sizing:border-box;margin:0;padding:0}
html,body{width:1200px;height:2655px;overflow:hidden}
body{font-family:"Montserrat",Arial,sans-serif;color:var(--ink);background:var(--white);position:relative}
.section{position:absolute;left:0;width:1200px}
.btn{position:absolute;display:flex;align-items:center;justify-content:center;background:var(--purple);color:var(--white);
  border-radius:22px;border-bottom:4px solid var(--purple-dark);font-weight:700;font-size:14px;letter-spacing:2.8px;text-transform:uppercase}
.rule{position:absolute;height:4px}

/* header */
.site-header{top:0;height:187px;background:var(--header-bg)}
.brand{position:absolute;left:160px;top:78px;display:flex;align-items:center;gap:10px;font-weight:800;font-size:20px;color:var(--purple);letter-spacing:1px}
.brand-dot{width:26px;height:26px;border-radius:50%;background:var(--yellow);flex:0 0 26px}
.header-call{position:absolute;right:155px;top:83px;font-size:12px;font-weight:500;letter-spacing:2.5px}
.main-nav{position:absolute;right:155px;top:114px;display:flex;gap:30px;font-size:12px;font-weight:700;letter-spacing:2.4px}

/* hero */
.hero{top:187px;height:382px;background:var(--yellow)}
.hero-photo{position:absolute;left:0;top:0;width:429px;height:382px;background:radial-gradient(circle at 50% 60%,#c8342a 0%,#8a2a22 35%,#111 70%)}
.hero-title{position:absolute;left:595px;top:52px;font-size:27px;font-weight:800;letter-spacing:6px;line-height:36px;color:var(--purple)}
.hero-rule{left:595px;top:152px;width:95px;background:var(--ink)}
.hero-quote{position:absolute;left:591px;top:193px;font-size:16.8px;font-weight:500;letter-spacing:3.4px;line-height:29px}
.hero-btn{left:591px;top:283px;width:325px;height:42px}

/* services */
.services{top:569px;height:802px;background:var(--blue)}
.services-title{position:absolute;left:228px;top:80px;font-size:28px;font-weight:800;letter-spacing:5px;line-height:37px;color:var(--white)}
.services-rule{left:228px;top:178px;width:95px;background:var(--ink)}
.service-grid{position:absolute;left:220px;top:241px;width:765px;background:var(--white);padding:6px 0 0}
.service-row + .service-row{margin-top:6px}
.service-images{display:grid;grid-template-columns:repeat(5,1fr);gap:8px;padding:0 6px 4px}
.service-art{height:162px}
.art-magic{background:linear-gradient(180deg,var(--blue-tile) 0%,var(--tile-mid) 28%,var(--blue-tile) 48%,var(--tile-dark) 62%,var(--tile-dark) 92%,var(--blue-tile) 100%)}
.art-clown{background:radial-gradient(ellipse 38% 48% at 50% 48%,var(--tile-light) 0%,#f3c8cf 45%,var(--tile-mid) 75%,var(--blue-tile) 100%)}
.service-labels{display:grid;grid-template-columns:repeat(5,1fr);background:var(--purple);height:26px;align-items:center;padding:0 6px}
.service-labels span{text-align:center;color:var(--white);font-size:11.5px;font-weight:700;letter-spacing:2px}
.services-btn{left:255px;top:694px;width:324px;height:42px}

/* welcome */
.welcome{top:1371px;height:423px;background:var(--gray-bg)}
.welcome-title{position:absolute;left:243px;top:88px;font-size:27px;font-weight:800;letter-spacing:5.6px;color:var(--heading-gray)}
.welcome-rule{left:243px;top:144px;width:95px;background:var(--heading-gray)}
.welcome-text{position:absolute;left:246px;top:189px;width:725px;font-size:12.5px;letter-spacing:2.1px;line-height:14.3px;color:#222}
.welcome-btn{left:244px;top:313px;width:325px;height:42px}

/* contact strip */
.contact-strip{top:1794px;height:174px;background:var(--yellow)}
.contact-item{position:absolute;top:70px;display:flex;align-items:center;gap:24px;font-size:11.5px;font-weight:600;letter-spacing:2.5px}
.contact-email{left:261px}
.contact-phone{left:790px}

/* form */
.hello{top:1968px;height:364px;background:var(--charcoal)}
.hello-title{position:absolute;left:0;width:1232px;top:28px;text-align:center;color:var(--white);font-size:19px;font-weight:500}
.hello-form{position:absolute;left:388px;top:77px;width:456px;border:1px solid #d8d8d8;color:#8a8a8a;font-size:7.5px;letter-spacing:1px}
.form-row{display:flex;border-bottom:1px solid #d8d8d8;height:34px;align-items:center}
.form-row > div{flex:1;padding-left:11px;height:100%;display:flex;align-items:center}
.form-row > div + div{border-left:1px solid #d8d8d8}
.form-message{height:124px;border-bottom:1px solid #d8d8d8;padding:11px}
.captcha-code{width:66px;height:14px;background:linear-gradient(90deg,#2e7a2e,#3f9a3f);opacity:.8}
.captcha-hint{font-size:5.5px;line-height:6px;color:#999;margin-left:28px;flex:0 0 60px!important}
.form-submit{height:33px;display:flex;align-items:center;justify-content:center;color:var(--white);font-weight:700;letter-spacing:2px}

/* footer */
.site-footer{top:2332px;height:235px;background:var(--white)}
.footer-brand{position:absolute;left:165px;top:80px;width:220px;display:flex;align-items:center;gap:12px;font-weight:800;font-size:20px;line-height:24px;color:var(--purple);letter-spacing:1px}
.footer-heading{position:absolute;top:74px;font-size:12px;font-weight:700;letter-spacing:2.6px}
.footer-about-title{left:430px}
.footer-about{position:absolute;left:430px;top:100px;width:345px;font-size:12px;line-height:14.4px;font-weight:500}
.footer-social-title{left:820px}
.social-list{position:absolute;left:815px;top:99px;display:flex;gap:6px}
.social-list span{width:31px;height:31px;border:1.5px solid var(--ink);border-radius:50%}

.legal{top:2567px;height:88px;background:var(--purple);color:var(--white);font-size:12px;font-weight:500}
.legal-copy{position:absolute;left:175px;top:45px}
.legal-links{position:absolute;right:174px;top:43px}
</style>
</head>
<body>

<header class="section site-header">
  <div class="brand"><span class="brand-dot"></span>Quindles Play Barn</div>
  <div class="header-call">CALL-555-010-247</div>
  <nav class="main-nav"><span>HOME</span><span>ABOUT US</span><span>FUN STUFF</span><span>TESTIMONIALS</span><span>NEWS</span><span>CONTACT US</span></nav>
</header>

<section class="section hero">
  <div class="hero-photo" role="img" aria-label="Photo of a clown in a red top hat and striped jacket on a black background"></div>
  <h1 class="hero-title">AWARD WINNING FAMILY<br>ENTERTAINMENT</h1>
  <div class="rule hero-rule"></div>
  <p class="hero-quote">"YOUR CHILDREN’S AND FAMILY’S<br>ENTERTAINMENT SPECIALIST"</p>
  <div class="btn hero-btn">Book your party today</div>
</section>

<section class="section services">
  <h2 class="services-title">WE GUARANTEED TO MAKE<br>YOUR PARTY A MEMORABLE ONE</h2>
  <div class="rule services-rule"></div>
  <div class="service-grid">
    <div class="service-row">
      <div class="service-images">
        <div class="service-art art-magic" role="img" aria-label="Illustration of a rabbit in a magic hat"></div>
        <div class="service-art art-clown" role="img" aria-label="Illustration of a jester clown"></div>
        <div class="service-art art-clown" role="img" aria-label="Illustration of a jester clown"></div>
        <div class="service-art art-magic" role="img" aria-label="Illustration of a rabbit in a magic hat"></div>
        <div class="service-art art-magic" role="img" aria-label="Illustration of a rabbit in a magic hat"></div>
      </div>
      <div class="service-labels"><span>MAGIC SHOWS</span><span>CIRCUS CLOWNS</span><span>CIRCUS CLOWNS</span><span>MAGIC SHOWS</span><span>MAGIC SHOWS</span></div>
    </div>
    <div class="service-row">
      <div class="service-images">
        <div class="service-art art-magic" role="img" aria-label="Illustration of a rabbit in a magic hat"></div>
        <div class="service-art art-clown" role="img" aria-label="Illustration of a jester clown"></div>
        <div class="service-art art-clown" role="img" aria-label="Illustration of a jester clown"></div>
        <div class="service-art art-magic" role="img" aria-label="Illustration of a rabbit in a magic hat"></div>
        <div class="service-art art-magic" role="img" aria-label="Illustration of a rabbit in a magic hat"></div>
      </div>
      <div class="service-labels"><span>MAGIC SHOWS</span><span>CIRCUS CLOWNS</span><span>CIRCUS CLOWNS</span><span>MAGIC SHOWS</span><span>MAGIC SHOWS</span></div>
    </div>
  </div>
  <div class="btn services-btn">View all our services</div>
</section>

<section class="section welcome">
  <h2 class="welcome-title">WELCOME TO QUINDLES PLAY BARN!</h2>
  <div class="rule welcome-rule"></div>
  <p class="welcome-text">Have you ever heard the expression "make your own fun"? Well, when you call Quindle's Play Barn, you don't have to! We make all the fun you'll need, and bring it straight to you. Clowns, Magicians, Face Painting, Balloon Animals, Jugglers, Party Princesses, Carnivals and much more, we create all of the fun that anyone could ever want! Our children's party entertainers appeal to your sense of fun regardless of age and we have a wide range of party services</p>
  <div class="btn welcome-btn">Read more about us</div>
</section>

<section class="section contact-strip">
  <div class="contact-item contact-email">
    <svg width="44" height="40" viewBox="0 0 44 40"><path d="M2 20 L42 2 L30 38 L20 26 Z" fill="var(--purple)"/><path d="M42 2 L20 26 L18 36 L14 24 Z" fill="var(--purple-dark)"/></svg>
    <span>INFO@QUINDLESPLAYBARN.COM</span>
  </div>
  <div class="contact-item contact-phone">
    <svg width="44" height="42" viewBox="0 0 44 42"><path d="M9 2 C4 4 2 9 4 15 C8 27 18 37 30 40 C36 42 40 39 42 35 L34 27 C32 26 30 27 28 29 C22 27 16 21 14 15 C16 13 17 11 16 9 Z" fill="var(--purple)"/></svg>
    <span>555-010-247</span>
  </div>
</section>

<section class="section hello">
  <h2 class="hello-title">Say Hello!</h2>
  <form class="hello-form">
    <div class="form-row"><div>YOUR NAME</div><div>YOUR EMAIL</div></div>
    <div class="form-message">YOUR MESSAGE*</div>
    <div class="form-row"><div>ENTER CAPTCHA*</div><div style="flex:0 0 70px;border-left:0"><span class="captcha-code" role="img" aria-label="Captcha word image"></span></div><div class="captcha-hint" style="border-left:0;padding-left:0">Not readable?<br>Change text.</div></div>
    <div class="form-submit">SUBMIT</div>
  </form>
</section>

<footer class="section site-footer">
  <div class="footer-brand"><span class="brand-dot"></span><span>Quindles<br>Play Barn</span></div>
  <h3 class="footer-heading footer-about-title">ABOUT US</h3>
  <p class="footer-about">Quindle has been performing professionally in the New York tri-state and Staten Island area since 1996 and has brought his special magic and memories to children's parties year after year and his popularity continues to grow with every fun and magical performance.</p>
  <h3 class="footer-heading footer-social-title">SOCIAL</h3>
  <div class="social-list"><span></span><span></span><span></span><span></span><span></span></div>
</footer>

<div class="section legal">
  <span class="legal-copy">Quindles Play Barn Entertainment © 2015. All Rights Reserved.</span>
  <span class="legal-links">Terms of Use | Privacy Policy</span>
</div>

</body>
</html>
```